Healthcare IT company looking for business card design

We develop IT systems for healthcare that significantly reduces cost and improves quality.

We want a business card design that is professional and clean, and using the colors in our logo.

Target Market(s)

Doctors and decision makers in the healthcare industry

Industry/Entity Type

Healthcare

Contact Information for Business Card

It should include
Name and title, address, telephone

Tobias Vrenholt, CEO
+46 712 418257
tobias@kelvaro.se

Font styles to use
Serif

Colors
0355a3
ed282f

Requirements
Must have
• Clean design
• Professional feel
Nice to have
• N/A
Should not have
• N/A

```html
<!DOCTYPE html>
<html lang="en">
<head>
<meta charset="utf-8">
<title>Kelvaro – Business Cards</title>
<link rel="stylesheet" href="https://fonts.googleapis.com/css2?family=Source+Sans+3:wght@400;600;700&display=swap">
<style>
  :root {
    --brand-blue: #0355a3;
    --brand-red: #ed282f;
    --card-white: #ffffff;
    --card-edge: #3a3a3a;
    --ink: #1c1c1c;
    --rule-grey: #a9a9a9;
    --stage: #efe9e1;
    --faint-red: #fbdcdd;
    --faint-blue: #dfe9f3;
  }
  * { box-sizing: border-box; margin: 0; padding: 0; }
  html, body { width: 1200px; height: 745px; overflow: hidden; }
  body {
    background: var(--stage);
    font-family: "Source Sans 3", "Myriad Pro", Arial, sans-serif;
    position: relative;
  }
  .card {
    position: absolute;
    width: 537px;
    height: 306px;
    border-radius: 28px;
    overflow: hidden;
  }
  .card--front {
    background: var(--card-white);
    border: 1px solid var(--card-edge);
    top: 49px;
  }
  .card--front-a { left: 39px; }
  .card--front-b { left: 613px; }
  .card--back {
    background: var(--brand-blue);
    left: 306px;
    top: 397px;
    border-radius: 24px;
  }
  .wordmark {
    position: absolute;
    display: flex;
    align-items: center;
    gap: 10px;
    font-weight: 700;
    line-height: 1;
    letter-spacing: -1px;
  }
  .card--front .wordmark {
    left: 38px;
    top: 20px;
    font-size: 92px;
    color: var(--brand-blue);
  }
  .wordmark__dot {
    width: 22px; height: 22px; border-radius: 50%;
    background: var(--brand-red);
    align-self: flex-start;
    margin-top: 8px;
  }
  .card--back .wordmark {
    left: 0; right: 0;
    justify-content: center;
    top: 74px;
    font-size: 100px;
    color: var(--card-white);
  }
  .card--back .wordmark__dot { background: var(--card-white); }
  .holder {
    position: absolute;
    right: 26px;
    top: 144px;
    text-align: right;
  }
  .holder__name {
    font-size: 21px;
    font-weight: 700;
    color: var(--brand-blue);
  }
  .divider {
    position: absolute;
    left: 0; right: 0;
    top: 169px;
    height: 3px;
    background: linear-gradient(to right, rgba(169,169,169,0) 0%, var(--rule-grey) 45%, var(--rule-grey) 100%);
  }
  .holder__title {
    position: absolute;
    right: 26px;
    top: 174px;
    font-size: 16px;
    color: var(--brand-red);
  }
  .contacts {
    position: absolute;
    right: 26px;
    top: 215px;
    list-style: none;
  }
  .contacts__item {
    display: flex;
    align-items: center;
    justify-content: flex-end;
    gap: 6px;
    font-size: 15px;
    color: var(--ink);
    height: 27px;
  }
  .contacts__icon { width: 18px; height: 18px; flex: none; }
  .faint-mark {
    position: absolute;
    left: 6px;
    top: 180px;
    width: 124px; height: 124px;
    border-radius: 50%;
    background: var(--faint-red);
    display: flex; align-items: center; justify-content: center;
  }
  .faint-mark::after {
    content: "";
    width: 50px; height: 50px; border-radius: 50%;
    background: var(--faint-blue);
    border: 6px solid var(--card-white);
  }
  .card--back .site {
    position: absolute;
    left: 0; right: 0;
    top: 208px;
    text-align: center;
    color: var(--card-white);
    font-size: 17px;
    letter-spacing: 3.5px;
  }
</style>
</head>
<body>

<section class="card card--front card--front-a">
  <div class="wordmark">Kelvaro<span class="wordmark__dot"></span></div>
  <div class="holder"><p class="holder__name">Tobias Vrenholt</p></div>
  <div class="divider"></div>
  <p class="holder__title">CEO</p>
  <ul class="contacts">
    <li class="contacts__item">
      <svg class="contacts__icon" viewBox="0 0 18 18"><rect width="18" height="18" rx="3" fill="#ed282f"/><path d="M6 4.5c-1 .6-1.5 1.6-1 3 1 2.6 3 4.6 5.5 5.6 1.3.5 2.4 0 3-1l-1.8-1.6-1.2.8c-1.4-.7-2.4-1.7-3-3l.8-1.2z" fill="#fff"/></svg>
      +46 712 418257
    </li>
    <li class="contacts__item">
      <svg class="contacts__icon" viewBox="0 0 18 18"><rect width="18" height="18" rx="3" fill="#ed282f"/><rect x="3.5" y="5.5" width="11" height="7.5" fill="none" stroke="#fff" stroke-width="1.4"/><path d="M3.5 5.5 9 10l5.5-4.5" fill="none" stroke="#fff" stroke-width="1.4"/></svg>
      tobias@kelvaro.se
    </li>
    <li class="contacts__item">
      <svg class="contacts__icon" viewBox="0 0 18 18"><rect width="18" height="18" rx="3" fill="#ed282f"/><circle cx="9" cy="9" r="5.2" fill="none" stroke="#fff" stroke-width="1.3"/><ellipse cx="9" cy="9" rx="2.2" ry="5.2" fill="none" stroke="#fff" stroke-width="1.1"/><path d="M3.8 9h10.4" stroke="#fff" stroke-width="1.1"/></svg>
      www.kelvaro.com
    </li>
  </ul>
</section>

<section class="card card--front card--front-b">
  <div class="faint-mark" aria-hidden="true"></div>
  <div class="wordmark">Kelvaro<span class="wordmark__dot"></span></div>
  <div class="holder"><p class="holder__name">Tobias Vrenholt</p></div>
  <div class="divider"></div>
  <p class="holder__title">CEO</p>
  <ul class="contacts">
    <li class="contacts__item">
      <svg class="contacts__icon" viewBox="0 0 18 18"><rect width="18" height="18" rx="4" fill="#0355a3"/><path d="M6 4.5c-1 .6-1.5 1.6-1 3 1 2.6 3 4.6 5.5 5.6 1.3.5 2.4 0 3-1l-1.8-1.6-1.2.8c-1.4-.7-2.4-1.7-3-3l.8-1.2z" fill="#fff"/></svg>
      +46 712 418257
    </li>
    <li class="contacts__item">
      <svg class="contacts__icon" viewBox="0 0 18 18"><rect width="18" height="18" rx="4" fill="#0355a3"/><rect x="3.5" y="5.5" width="11" height="7.5" fill="none" stroke="#fff" stroke-width="1.4"/><path d="M3.5 5.5 9 10l5.5-4.5" fill="none" stroke="#fff" stroke-width="1.4"/></svg>
      tobias@kelvaro.se
    </li>
    <li class="contacts__item">
      <svg class="contacts__icon" viewBox="0 0 18 18"><rect width="18" height="18" rx="4" fill="#0355a3"/><circle cx="9" cy="9" r="5.2" fill="none" stroke="#fff" stroke-width="1.3"/><ellipse cx="9" cy="9" rx="2.2" ry="5.2" fill="none" stroke="#fff" stroke-width="1.1"/><path d="M3.8 9h10.4" stroke="#fff" stroke-width="1.1"/></svg>
      www.kelvaro.com
    </li>
  </ul>
</section>

<section class="card card--back">
  <div class="wordmark">Kelvaro<span class="wordmark__dot"></span></div>
  <p class="site">www.kelvaro.com</p>
</section>

</body>
</html>
```